Instagram Story & Feed Template Design

Hey there,

We are looking for someone who can design a template for us to use each week to promote our podcast on Instagram stories and Instagram feed.

The priority of this job is the graphic design elements of the Instagram Story and Instagram Feed. (These design files will then be given to an animator who will convert these into a video template in Premiere Pro).

The podcast is called The Corinne Valdetti Show which you can view here: https://podlisten.example/au/show/the-corinne-valdetti-show/id5830472916

Here is an example of how we are currently doing the Instagram Feed post. This follows the classic 'meme' style of Instagram feed post. It converts well but it's ugly :)

https://www.snapvista.example/tv/QkR7mZ2LwX9/?utm_source=sv_web_copy_link

Each week in the template we would change the:

- Title of the show (see root ledger example)
- Name of guest
- Episode #
- Episode link (eg, corinnevaldetti.example/375)
- Photo of the guest (if this ends up being a part of the winning design)
- The feed preview Cover Image of the Instagram feed post

Instagram feed dimensions: 1080 x 1080 px
Instagram story dimensions: 1080 x 1920 px

Target market is 90% female, interested in health, wellness and spirituality.

This is an example of how someone else is doing something similar (root ledger): https://www.snapvista.example/tv/ZPWNdUEJopT/?utm_source=sv_web_copy_link

This example can be improved by always starting with a quick 5-sec highlight of the video to get their attention (see Corinne's example above), and a prominent catchy heading (for the Feed post).

We have provided brand guidelines/style guide, logo and colours as well as a screenshot of the new website design that launches in the next week, so you can see what we are aiming for visually.

Examples of some animations we liked are as follows. While this job is not about animating, but design, this may help with ideas as to what we are looking for.

- https://clipmarket.example/item/driftly-fcpx-motion-pack-for-reels/48120377
- https://clipmarket.example/item/podcast-social-pack-vertical-and-square/49301562

Overall, the design must...

- Follow brand guidelines (attached)
- Use new imagery of Corinne (attached)
- Display clearly on Instagram feeds and get people's attention
- Use the Corinne Valdetti show logo

Thanks :)

Tom

```html
<!DOCTYPE html>
<html lang="en">
<head>
<meta charset="utf-8">
<title>The Corinne Valdetti Show – Episode 112 Story</title>
<link href="https://fonts.googleapis.com/css2?family=Libre+Baskerville:wght@400;700&family=Nunito+Sans:wght@400;700;800&display=swap" rel="stylesheet">
<style>
  :root {
    --gold: #d9b955;
    --slate: #5f6368;
    --ink: #2d2d2d;
    --logo: #b39a72;
    --paper: #ffffff;
    --tag-bg: rgba(40, 40, 40, 0.82);
    --verified: #3b8df0;
  }
  * { margin: 0; padding: 0; box-sizing: border-box; }
  html, body { width: 675px; height: 1200px; overflow: hidden; background: var(--paper); }
  .story {
    position: relative;
    width: 675px;
    height: 1200px;
    overflow: hidden;
    background: var(--paper);
    font-family: "Libre Baskerville", Georgia, serif;
    color: var(--ink);
  }
  .show-name {
    position: absolute;
    left: 24px; top: 84px;
    width: 232px; height: 127px;
    display: flex;
    flex-direction: column;
    justify-content: center;
    align-items: flex-end;
    color: var(--logo);
    font-family: "Libre Baskerville", Georgia, serif;
    font-weight: 400;
    font-size: 21px;
    line-height: 31px;
    letter-spacing: 2px;
    text-align: right;
    text-transform: uppercase;
  }
  .divider {
    position: absolute;
    left: 272px; top: 84px;
    width: 4px; height: 127px;
    background: var(--gold);
  }
  .episode-title {
    position: absolute;
    left: 294px; top: 78px;
    font-weight: 700;
    font-size: 34px;
    line-height: 49px;
    color: var(--slate);
    white-space: nowrap;
    letter-spacing: -1.2px;
  }
  .episode-title .accent { color: var(--gold); }
  .hook-band {
    position: absolute;
    left: 0; top: 282px;
    width: 675px; height: 168px;
    background: var(--gold);
    color: var(--paper);
    text-align: center;
  }
  .hook-band .hook-head {
    font-weight: 700;
    font-size: 58px;
    line-height: 60px;
    margin-top: 18px;
    letter-spacing: -2px;
  }
  .hook-band .hook-sub {
    font-weight: 400;
    font-size: 31px;
    line-height: 40px;
    margin-top: 4px;
    letter-spacing: -0.8px;
  }
  .portrait { position: absolute; top: 458px; }
  .portrait--host {
    left: 15px; width: 326px; height: 406px;
    background: linear-gradient(160deg, #e9e8e2 0%, #c9c2b6 45%, #3a302b 75%, #d7cfc4 100%);
  }
  .portrait--guest {
    left: 356px; width: 302px; height: 410px;
    background: linear-gradient(180deg, #6e6a62 0%, #d8d9da 30%, #a7a9ab 60%, #3a3b3e 100%);
  }
  .handle-tag {
    position: absolute;
    top: 342px;
    height: 37px;
    border-radius: 8px;
    background: var(--tag-bg);
    color: var(--paper);
    font-family: "Nunito Sans", Arial, sans-serif;
    font-size: 24px;
    line-height: 37px;
    padding: 0 12px;
    display: flex;
    align-items: center;
    gap: 10px;
    white-space: nowrap;
  }
  .portrait--host .handle-tag { left: 16px; width: 294px; }
  .portrait--guest .handle-tag { left: 11px; width: 279px; }
  .verified-dot {
    width: 22px; height: 22px; border-radius: 50%;
    background: var(--verified);
    flex: none;
  }
  .listen-cta {
    position: absolute;
    left: 0; top: 928px;
    width: 675px;
    text-align: center;
    font-family: "Nunito Sans", Arial, sans-serif;
    font-weight: 800;
    font-size: 21px;
    line-height: 27px;
    color: var(--ink);
    letter-spacing: -0.3px;
  }
  .platforms {
    position: absolute;
    left: 0; top: 1025px;
    width: 675px;
    display: flex;
    justify-content: center;
    gap: 34px;
    font-family: "Nunito Sans", Arial, sans-serif;
    font-weight: 700;
    font-size: 26px;
    color: var(--ink);
  }
  .platform { display: flex; align-items: center; gap: 8px; }
  .platform-dot { width: 34px; height: 34px; border-radius: 50%; background: var(--ink); }
  .footer-band {
    position: absolute;
    left: 0; top: 1094px;
    width: 675px; height: 35px;
    background: var(--gold);
    color: var(--paper);
    text-align: center;
    font-family: "Nunito Sans", Arial, sans-serif;
    font-weight: 800;
    font-size: 21px;
    line-height: 35px;
    letter-spacing: 2.5px;
    white-space: nowrap;
  }
</style>
</head>
<body>
  <main class="story">
    <div class="show-name">
      <span>The Corinne</span>
      <span>Valdetti</span>
      <span>Show</span>
    </div>
    <div class="divider"></div>
    <h1 class="episode-title">
      <span class="accent">ON THE ETHICS</span><br>
      BEHIND DIETARY<br>
      CHOICES
    </h1>

    <section class="hook-band">
      <p class="hook-head">WATCH THIS</p>
      <p class="hook-sub">If you are ready to help<br>save the planet from plastic</p>
    </section>

    <div class="portrait portrait--host" role="img" aria-label="Portrait photo of the host in a black lace dress by a window">
      <div class="handle-tag">@corinnevaldetti <span class="verified-dot"></span></div>
    </div>
    <div class="portrait portrait--guest" role="img" aria-label="Portrait photo of the guest in a grey ruffled top on a beach">
      <div class="handle-tag">@wholesomeroots</div>
    </div>

    <p class="listen-cta">LISTEN TO THE FULL EPISODE<br>WITH DELIA MARSH<br>ON</p>

    <div class="platforms">
      <span class="platform"><span class="platform-dot"></span>Tunebox</span>
      <span class="platform"><span class="platform-dot"></span>Streamly</span>
    </div>

    <footer class="footer-band">EPISODE 112 | corinnevaldetti.example/375</footer>
  </main>
</body>
</html>
```